Website for Company to help with House Restoration from Hurricane Damage

Crisp, Clean and Professional!

I need a FRONT page for a website. I need it created in photoshop with the layers intact. We DO NOT need the HTML or DRB for the site. Simply the design. Any fonts you use will need to be included if they are not standard. Please make sure any fonts you use in the body of the text are available for use on Google Fonts.

I have attached a word doc that lists the menu items and additional instructions.

A little about the company - after Hurricane Marlow - DRB developed a system which allows the house to be raised, the Tremlets installed, and the house reset on the Tremlets without the expense of moving the house or driving new pilings. This option can be installed in a matter of days with limited space and at a lower construction cost.

Please refer to the attached musthaves.doc and images that are included.

The main page must incorporate the menu, the attached photos w/ text underneath (text is in the word doc attached), and the text included in the word doc.

Standard footer with contact info as well.

If you have questions please contact us!
Updates

Designs are due by Friday! We will pick one this weekend.  We are unable to change it from 10 days to 5.  Thank you!!!

Target Market(s)

People who lost their homes or businesses due to a hurricane.

Industry/Entity Type

Construction

Requirements
Must have
• See attached musthaves.doc

```html
<!DOCTYPE html>
<html lang="en">
<head>
<meta charset="utf-8">
<title>Durable Raise Builders, LLC (DRB)</title>
<link rel="stylesheet" href="https://fonts.googleapis.com/css2?family=Oxygen:wght@300;400&family=Niconne&display=swap">
<style>
  :root {
    --brand-green: #3b4a24;
    --accent-green: #4f7d10;
    --bar-green: #7ea23a;
    --menu-navy: #22345a;
    --menu-dark: #1f2327;
    --text-light: #f2f2f2;
    --text-dark: #1c1f26;
    --panel-dark: rgba(28, 30, 44, 0.72);
    --panel-footer: rgba(150, 156, 172, 0.62);
  }
  * { box-sizing: border-box; margin: 0; padding: 0; }
  html, body { width: 1200px; height: 1064px; overflow: hidden; }
  body {
    position: relative;
    font-family: "Oxygen", Arial, sans-serif;
    color: var(--text-light);
    background: #333;
  }
  .backdrop {
    position: absolute; inset: 0;
    background: linear-gradient(180deg, #a99bbd 0%, #c9a8bf 18%, #8f7f96 32%, #4f5169 42%, #2c3450 62%, #2a3246 80%, #3a3f52 100%);
  }
  .brand {
    position: absolute; left: 473px; top: 0; width: 254px; height: 107px;
    background: var(--brand-green);
    display: flex; flex-direction: column; align-items: center; justify-content: center; gap: 4px;
    color: #f4f1e4; font-weight: 400;
  }
  .brand-mark { width: 22px; height: 22px; background: #b8cf8a; }
  .brand-name { font-size: 19px; letter-spacing: 0.2px; }
  .brand-sub { font-size: 11px; }
  .hero {
    position: absolute; left: 220px; top: 107px; width: 761px; height: 320px;
    border-top: 6px solid var(--brand-green);
    border-bottom: 2px solid #fff;
    background: linear-gradient(180deg, #b8a3b5 0%, #d7a8a0 12%, #a9929a 24%, #7f7b8a 50%, #6d6a73 70%, #5b4f48 85%, #3e3632 100%);
  }
  .slogan {
    position: absolute; left: 0; height: 32px;
    font-family: "Niconne", cursive; font-size: 21px;
    padding-left: 16px; line-height: 32px; color: var(--text-dark);
    background: rgba(255, 255, 255, 0.72);
  }
  .slogan--safer { top: 103px; width: 186px; }
  .slogan--stronger { top: 141px; width: 250px; color: #fff; background: linear-gradient(90deg, var(--bar-green) 0%, #86a93e 92%, rgba(126,162,58,0.4) 100%); }
  .slogan--memories { top: 182px; width: 337px; }
  .main-nav { position: absolute; right: 0; top: 72px; list-style: none; }
  .main-nav li {
    height: 27px; margin-left: auto; margin-bottom: 0;
    font-size: 10.5px; letter-spacing: 0.4px; text-transform: uppercase;
    line-height: 27px; text-align: right; padding-right: 24px; color: #fff;
  }
  .main-nav li:nth-child(odd) { background: var(--menu-navy); }
  .main-nav li:nth-child(even) { background: var(--menu-dark); }
  .nav-home { width: 95px; }
  .nav-services { width: 110px; }
  .nav-about { width: 131px; }
  .nav-product { width: 166px; }
  .nav-design { width: 166px; }
  .nav-contact { width: 121px; }
  .intro {
    position: absolute; left: 220px; top: 427px; width: 761px; height: 416px;
    background: var(--panel-dark);
    padding: 33px 17px 0 16px;
  }
  .intro-title { font-size: 16px; font-weight: 400; }
  .intro-title small, .footer-title small { font-size: 12px; }
  .intro-rule {
    margin-top: 10px; height: 2px; width: 727px;
    background: linear-gradient(90deg, var(--accent-green) 0 80px, #e8e8e8 80px);
  }
  .intro-copy {
    margin: 23px 0 0 2px; width: 727px;
    font-size: 10.5px; font-weight: 300; line-height: 21px; text-align: justify;
  }
  .intro-copy + .intro-copy { margin-top: 21px; }
  .read-more {
    position: absolute; left: 643px; top: 356px; width: 101px; height: 29px;
    background: var(--accent-green); color: #fff;
    font-size: 10px; text-transform: uppercase; line-height: 29px; text-align: center;
  }
  .read-more span { font-size: 12px; margin-left: 4px; }
  .site-footer {
    position: absolute; left: 220px; top: 843px; width: 761px; height: 164px;
    background: var(--panel-footer); color: var(--text-dark);
  }
  .footer-title { position: absolute; left: 18px; top: 23px; font-size: 13px; font-weight: 400; }
  .contact { position: absolute; left: 37px; top: 63px; font-size: 10.5px; line-height: 21px; font-style: normal; }
  .sitemap-title { position: absolute; left: 423px; top: 22px; font-size: 14px; font-weight: 400; }
  .sitemap { position: absolute; left: 431px; top: 48px; list-style: none; font-size: 10.5px; line-height: 17px; }
  .sitemap li::before { content: "::"; font-size: 8px; margin-right: 6px; color: #444; }
</style>
</head>
<body>
  <div class="backdrop" role="img" aria-label="Blurred beach at sunset behind the page"></div>

  <header class="brand">
    <span class="brand-mark"></span>
    <span class="brand-name">Durable Raise Builders</span>
    <span class="brand-sub">LLC (DRB)</span>
  </header>

  <section class="hero" role="img" aria-label="Photo of a father and toddler on a beach at sunset, boats on the water">
    <p class="slogan slogan--safer">Rebuild Safer</p>
    <p class="slogan slogan--stronger">Stronger</p>
    <p class="slogan slogan--memories">Better to build new lasting memories</p>
    <ul class="main-nav">
      <li class="nav-home">Home</li>
      <li class="nav-services">Services</li>
      <li class="nav-about">About Us</li>
      <li class="nav-product">Product Specifications</li>
      <li class="nav-design">Design Documentation</li>
      <li class="nav-contact">Contact Us</li>
    </ul>
  </section>

  <main class="intro">
    <h1 class="intro-title">Durable Raise Builders, <small>LLC (DRB)</small></h1>
    <div class="intro-rule"></div>
    <p class="intro-copy">Systems for extending the height of existing piles are not available on today’s market.  Durable Raise Builders, LLC (DRB) has developed two systems to allow for Piles to be extended that provide superior structural support without corrosion and maintenance concerns.  We provided two systems, a complete system, Pile Cap Extension Tremlets, and Pile Splice.  These two systems allow a home to be raised to by up to 54”, higher extensions possible with additional design consideration for lateral support. Shown below is the full Piling Extension system, which connects to the top of the existing pile. The system modular and can be cut to meet specific needs of the home.</p>
    <p class="intro-copy">Our Patented Piling system has been designed to withstand the corrosive environment of beach communities. The salt water and windblown sand corrodes unprotected materials, and yes, even stainless steel. Our system utilizes a high strength carbon fiber material that is corrosion proof from salt water and UV proof.  The system will not erode, decay or loose strength over time. The system has three installation conditions, for raising a house on existing pilings, repairing damaged pilings, and for connecting new pilings to floor joists in new construction. The three options are generally described here.</p>
    <a class="read-more">Read More <span>&gt;&gt;</span></a>
  </main>

  <footer class="site-footer">
    <h2 class="footer-title">Durable Raise Builders, <small>LLC (DRB)</small></h2>
    <address class="contact">
      P.O. Box : 40512,  Harbor Valley ,<br>
      PA : 18000-0140 - (555) 014-2290<br>
      Email : sales@durableraise.com
    </address>
    <h2 class="sitemap-title">Site Map</h2>
    <ul class="sitemap">
      <li>Home</li>
      <li>Services</li>
      <li>About Us</li>
      <li>Product Specifications</li>
      <li>Design Documentation</li>
      <li>Contact Us</li>
    </ul>
  </footer>
</body>
</html>
```